design for wedding expo stand to attract brides - help me get out of the 1980's

Design a print for an expo stand, we are a wedding videography company that regularly exhibits at wedding expos. The stand we are purchasing is 2700mm x 2300mm curved. The stand will usually have a 50" TV in front of it but I would like some images / graphic of a wedding / bride or bride & groom etc ** I only have 4 days to choose
Updates

I need to make a choice by the 31st of June

Target Market(s)

expo attendees, mainly prospective brides

Colors

Requirements
Must have
• logo, preferably horizontal one, any critical information / graphics should be on the outer 3rd of the stand - The stand is 2700mm wide and the TV is 1200mm wide, that leaves 1500mm on one side of the TV. The stand is 2300mm high and the Tv is 700mm - that leaves around 900mm at the top. I think the best option for the design is to have the TV on the left or right hand side rather than in the middle to allow more room for the graphic.
Nice to have
• the stand will usually have a 50"TV in front of it so either the logo or the question "you spend a long time planning your wedding, how do you plan to remember it?" or both should be in the top 25% of the display. I can sit the TV under that but I may have a smaller TV in the future so the stand should have some image/design behind it or around the edges
Should not have
• please don't include a TV in the design, it's doesn't make sense.

```html
<!DOCTYPE html>
<html lang="en">
<head>
<meta charset="utf-8">
<title>Keepsake Reel – Expo Stand Print</title>
<link href="https://fonts.googleapis.com/css2?family=Lato:wght@400;700;900&display=swap" rel="stylesheet">
<style>
  :root {
    --ink-navy: #1d3c78;
    --sky-blue: #1b98d5;
    --deep-blue: #1f3f9a;
    --light-blue: #5cc3e2;
    --sun-orange: #ef8a00;
    --gold: #f2c230;
    --paper: #ffffff;
    --backdrop: #000000;
  }
  * { margin: 0; padding: 0; box-sizing: border-box; }
  html, body {
    width: 1200px; height: 1200px; overflow: hidden;
    background: var(--backdrop);
    font-family: "Lato", Arial, sans-serif;
  }
  .stand-print {
    position: absolute;
    left: 50px; top: 131px;
    width: 1100px; height: 937px;
    background: var(--paper);
    overflow: hidden;
  }
  .stand-print svg.artwork {
    position: absolute; inset: 0;
    width: 100%; height: 100%;
  }
  .brand {
    position: absolute;
    left: 40px; top: 34px;
    display: flex; align-items: center; gap: 22px;
  }
  .brand-mark {
    width: 132px; height: 140px;
    background: var(--sky-blue);
    border-radius: 6px;
  }
  .brand-words { display: flex; flex-direction: column; }
  .brand-name {
    font-weight: 900;
    font-size: 50px;
    line-height: 1;
    color: var(--ink-navy);
    white-space: nowrap;
  }
  .brand-tagline {
    align-self: flex-end;
    margin-top: 8px;
    margin-right: 30px;
    font-size: 26px;
    color: var(--sky-blue);
    letter-spacing: 1px;
    white-space: nowrap;
  }
  .headline {
    position: absolute;
    color: var(--sky-blue);
    font-size: 31px;
    line-height: 34.5px;
    letter-spacing: 2px;
  }
  .headline span { display: block; white-space: nowrap; }
  .headline .accent { display: inline; color: var(--sun-orange); font-weight: 700; }
  .headline--planning { left: 122px; top: 219px; }
  .headline--planning .indent { padding-left: 129px; }
  .headline--remember { left: 56px; top: 393px; }
  .headline--remember .indent { padding-left: 20px; }
</style>
</head>
<body>
  <main class="stand-print">
    <svg class="artwork" viewBox="0 0 862 734" preserveAspectRatio="none">
      <defs>
        <linearGradient id="curveBand" x1="0" y1="0" x2="0" y2="1">
          <stop offset="0" stop-color="#1f3f9a"/>
          <stop offset="0.5" stop-color="#5cc3e2"/>
          <stop offset="0.85" stop-color="#1f3f9a"/>
          <stop offset="1" stop-color="#1f3f9a"/>
        </linearGradient>
        <linearGradient id="goldEdge" x1="0" y1="0" x2="0" y2="1">
          <stop offset="0" stop-color="#f2c230" stop-opacity="0"/>
          <stop offset="0.55" stop-color="#f2c230" stop-opacity="0.55"/>
          <stop offset="1" stop-color="#f2c230"/>
        </linearGradient>
        <linearGradient id="photoBase" x1="0" y1="0" x2="0.35" y2="1">
          <stop offset="0" stop-color="#6f7f66"/>
          <stop offset="0.22" stop-color="#a9b2a6"/>
          <stop offset="0.45" stop-color="#e6e8e8"/>
          <stop offset="0.75" stop-color="#f7f7f6"/>
          <stop offset="1" stop-color="#efebe6"/>
        </linearGradient>
        <radialGradient id="photoSuit" cx="0.62" cy="0.28" r="0.28">
          <stop offset="0" stop-color="#1c2238" stop-opacity="0.75"/>
          <stop offset="0.6" stop-color="#2c3f7a" stop-opacity="0.35"/>
          <stop offset="1" stop-color="#2c3f7a" stop-opacity="0"/>
        </radialGradient>
        <radialGradient id="photoLeaves" cx="0.45" cy="0.65" r="0.55">
          <stop offset="0" stop-color="#d08a3a" stop-opacity="0.35"/>
          <stop offset="1" stop-color="#d08a3a" stop-opacity="0"/>
        </radialGradient>
      </defs>
      <path class="curve-band" d="M536,0 C430,140 330,360 311,734 L862,734 L862,0 Z" fill="url(#curveBand)"/>
      <path class="curve-gold" d="M548,0 C445,150 356,360 345,734 L420,734 L862,0 Z" fill="url(#goldEdge)"/>
      <g class="hero-photo" role="img"
        aria-label="Photograph: bride and groom lying on a lawn seen from above, her white gown and veil spread out, autumn leaves scattered around">
        <path d="M560,0 C462,150 380,360 378,734 L862,734 L862,0 Z" fill="url(#photoBase)"/>
        <path d="M560,0 C462,150 380,360 378,734 L862,734 L862,0 Z" fill="url(#photoSuit)"/>
        <path d="M560,0 C462,150 380,360 378,734 L862,734 L862,0 Z" fill="url(#photoLeaves)"/>
      </g>
    </svg>

    <div class="brand">
      <span class="brand-mark"></span>
      <div class="brand-words">
        <span class="brand-name">KEEPSAKE REEL</span>
        <span class="brand-tagline">wedding films</span>
      </div>
    </div>

    <p class="headline headline--planning">
      <span>You spend a</span>
      <span class="indent">long time</span>
      <span>planning for</span>
      <span>your <span class="accent">wedding</span>,</span>
    </p>

    <p class="headline headline--remember">
      <span>How do you</span>
      <span>plan to</span>
      <span class="indent"><span class="accent">remember</span> it?</span>
    </p>
  </main>
</body>
</html>
```